Lorn's Cleaners new delivery postcard

We need to advertise for our new pick up and delivery dry cleaning/laundry service.
Mens Business Shirts $2.00
Pants $4.50
Skirts $5.00
Dry Clean Shirt/Blouse $5.00
Dress $9.00
2 Piece Suits $9.00
Updates
We would like to use a 5x7 size postcard, printed on both sides. We would like to add a discount to the card for 25% off of their first order, with the flyer.
We are a famly run dry cleaners. My name is Paula Brandt and my cell # is 614-372-0481. We are trying to expand our business to include free pick and delivery.
If possible can you use the logo I sent some where on the postcard? The phone # for the store is 614-205-3967.
Reason: Still need to get partners approval.
Industry/Entity Type
Business

```html
<!DOCTYPE html>
<html lang="en">
<head>
<meta charset="utf-8">
<title>Paula Brandt Dry Cleaning – Delivery Postcard</title>
<link rel="stylesheet" href="https://fonts.googleapis.com/css2?family=Roboto:ital,wght@0,400;0,700;0,900;1,700;1,900&family=Roboto+Condensed:wght@400;700&display=swap">
<style>
  :root {
    --teal: #12a3c4;
    --navy: #1d4f9c;
    --band-blue: #1f5fb5;
    --red: #e0242a;
    --yellow: #ffe21a;
    --ink: #3a3a3a;
    --paper: #ffffff;
  }
  * { margin: 0; padding: 0; box-sizing: border-box; }
  html, body { width: 893px; height: 1200px; overflow: hidden; background: var(--paper); }
  .postcard {
    position: relative;
    width: 893px;
    height: 1200px;
    background: var(--paper);
    font-family: "Roboto", Arial, sans-serif;
    overflow: hidden;
  }
  .header { position: absolute; top: 28px; left: 0; width: 100%; text-align: center; }
  .brand-name {
    font-weight: 900;
    font-size: 96px;
    letter-spacing: 2px;
    color: var(--teal);
    line-height: 1;
  }
  .service-line {
    display: inline-block;
    margin-top: 10px;
    padding-bottom: 10px;
    font-family: "Roboto Condensed", Arial, sans-serif;
    font-size: 42px;
    line-height: 1.1;
    color: var(--ink);
    letter-spacing: 1px;
    border-bottom: 5px solid var(--teal);
  }
  .hero-photo {
    position: absolute;
    top: 215px; left: 0;
    width: 893px; height: 500px;
    background: linear-gradient(90deg, #e4e7eb 0%, #8fb0d4 25%, #2c6fb8 55%, #1e4f98 80%, #e6e8eb 100%);
  }
  .offer-badge {
    position: absolute;
    left: 45px; top: 560px;
    width: 240px; height: 240px;
    border-radius: 50%;
    background: var(--red);
    border: 8px solid var(--paper);
    color: var(--paper);
    display: flex; flex-direction: column; align-items: center; justify-content: center;
    text-align: center;
    z-index: 2;
  }
  .offer-badge .percent { font-size: 70px; font-weight: 700; line-height: 1; }
  .offer-badge .off { font-size: 46px; font-weight: 900; line-height: 1; }
  .offer-badge .terms { font-family: "Roboto Condensed", Arial, sans-serif; font-size: 20px; font-weight: 700; line-height: 1.1; margin-top: 6px; }
  .delivery-band {
    position: absolute;
    left: 260px; top: 690px;
    width: 633px; height: 110px;
    background: var(--band-blue);
    display: flex; align-items: center;
    padding-left: 60px;
    z-index: 1;
  }
  .delivery-band svg { flex: none; margin-right: 26px; }
  .delivery-band .headline {
    color: var(--yellow);
    font-weight: 900; font-style: italic;
    font-size: 38px; line-height: 1.05;
  }
  .benefits { position: absolute; left: 52px; top: 822px; list-style: none; }
  .benefits li {
    display: flex; align-items: center;
    height: 36px;
    font-weight: 900; font-style: italic;
    font-size: 30px; color: var(--teal);
    margin-bottom: 6px;
  }
  .benefits svg { margin-right: 16px; flex: none; }
  .clothes-photo {
    position: absolute;
    left: 545px; top: 815px;
    width: 335px; height: 290px;
    background: linear-gradient(180deg, #f4c83a 0%, #e07a3a 22%, #d24a7a 40%, #7a5cc2 55%, #3fa0d8 70%, #5cb85a 85%, #c0392b 100%);
    opacity: .85;
  }
  .call-box { position: absolute; left: 52px; top: 994px; width: 400px; }
  .call-label {
    font-family: "Roboto Condensed", Arial, sans-serif;
    font-size: 22px; line-height: 1.1; color: var(--ink); text-align: center;
  }
  .phone {
    margin-top: 4px;
    background: var(--navy);
    color: var(--paper);
    font-weight: 700; font-size: 50px; line-height: 1.2;
    text-align: center; padding: 2px 0 4px;
  }
  .family-line {
    position: absolute; left: 0; top: 1122px; width: 100%;
    text-align: center;
    color: var(--red); font-weight: 900; font-size: 40px; line-height: 1.1;
  }
</style>
</head>
<body>
<main class="postcard">
  <header class="header">
    <h1 class="brand-name">PAULA BRANDT</h1>
    <p class="service-line">DRY CLEANING/LAUNDRY SERVICE</p>
  </header>

  <div class="hero-photo" role="img" aria-label="Photo of a hand pulling a blue towel out of a front-loading washing machine"></div>

  <div class="offer-badge">
    <div class="percent">25%</div>
    <div class="off">OFF</div>
    <div class="terms">ON YOUR<br>FIRST ORDER</div>
  </div>

  <div class="delivery-band">
    <svg width="74" height="44" viewBox="0 0 74 44" aria-hidden="true">
      <rect x="0" y="4" width="44" height="28" fill="#fff"/>
      <path d="M46 12h14l10 11v9H46z" fill="#fff"/>
      <circle cx="14" cy="36" r="7" fill="#fff" stroke="#1f5fb5" stroke-width="3"/>
      <circle cx="58" cy="36" r="7" fill="#fff" stroke="#1f5fb5" stroke-width="3"/>
    </svg>
    <p class="headline">NEW PICK UP &amp;<br>DELIVERY SERVICE</p>
  </div>

  <ul class="benefits">
    <li><svg width="28" height="28" viewBox="0 0 30 30" aria-hidden="true"><path d="M3 16l8 8L27 6" fill="none" stroke="#1f5fb5" stroke-width="6" stroke-linecap="round" stroke-linejoin="round"/></svg>QUALITY CARE</li>
    <li><svg width="28" height="28" viewBox="0 0 30 30" aria-hidden="true"><path d="M3 16l8 8L27 6" fill="none" stroke="#1f5fb5" stroke-width="6" stroke-linecap="round" stroke-linejoin="round"/></svg>SPOTLESS GUARANTEE</li>
    <li><svg width="28" height="28" viewBox="0 0 30 30" aria-hidden="true"><path d="M3 16l8 8L27 6" fill="none" stroke="#1f5fb5" stroke-width="6" stroke-linecap="round" stroke-linejoin="round"/></svg>PICKUP AND DELIVERY</li>
    <li><svg width="28" height="28" viewBox="0 0 30 30" aria-hidden="true"><path d="M3 16l8 8L27 6" fill="none" stroke="#1f5fb5" stroke-width="6" stroke-linecap="round" stroke-linejoin="round"/></svg>RELIABLE AND AFFORDABLE</li>
  </ul>

  <div class="clothes-photo" role="img" aria-label="Photo of a stack of neatly folded colourful clothes"></div>

  <div class="call-box">
    <p class="call-label">CALL MS. PAULA</p>
    <p class="phone">614-205-3967</p>
  </div>

  <p class="family-line">WE ARE A FAMLY RUN DRY CLEANERS</p>
</main>
</body>
</html>
```